Melissa Tarnow Personal Business Card

I like orange. It's would better if my card have an orange background
Address: 4720 Halberd Lane #318
San Jose
California
US
Tel: 4085172946

Industry/Entity Type

Business

```html
<!DOCTYPE html>
<html lang="en">
<head>
<meta charset="utf-8">
<title>Melissa Tarnow – Business Card</title>
<link rel="stylesheet" href="https://fonts.googleapis.com/css2?family=Alegreya+Sans:wght@400;500&family=Alegreya+Sans+SC:wght@400;500&family=Cormorant+Garamond:ital,wght@1,500&display=swap">
<style>
  :root {
    --card-orange: #f5831f;
    --card-orange-deep: #ee7618;
    --ink: #231f20;
    --white: #ffffff;
  }
  html, body {
    margin: 0;
    padding: 0;
    width: 667px;
    height: 1200px;
    overflow: hidden;
    background: var(--card-orange);
  }
  .card {
    position: relative;
    width: 667px;
    height: 1200px;
    overflow: hidden;
    background: var(--card-orange);
  }
  .card__pattern {
    position: absolute;
    inset: 0;
    background: radial-gradient(circle at 50% 45%, var(--card-orange) 0%, var(--card-orange-deep) 100%);
  }
  .card__badge {
    position: absolute;
    left: 0;
    top: 0;
    width: 667px;
    height: 700px;
  }
  .text-block {
    position: absolute;
    left: 0;
    width: 100%;
    text-align: center;
    transform: translateY(-50%);
    margin: 0;
    white-space: nowrap;
  }
  .badge__name {
    top: 402px;
    font-family: "Alegreya Sans SC", sans-serif;
    font-weight: 400;
    font-size: 33px;
    line-height: 1;
    color: var(--white);
    letter-spacing: 3.5px;
  }
  .label {
    font-family: "Cormorant Garamond", serif;
    font-style: italic;
    font-weight: 500;
    font-size: 27px;
    line-height: 1;
    color: var(--white);
    letter-spacing: 1px;
  }
  .label--address { top: 729px; }
  .label--tel { top: 1017px; }
  .contact-line {
    font-family: "Alegreya Sans SC", sans-serif;
    font-weight: 500;
    font-size: 34px;
    line-height: 1;
    color: var(--ink);
    letter-spacing: 1.5px;
    text-transform: lowercase;
    font-variant-numeric: oldstyle-nums;
  }
  .address-street { top: 779px; }
  .address-city { top: 821px; }
  .address-state { top: 866px; }
  .address-country { top: 911px; }
  .phone {
    top: 1060px;
    font-family: "Alegreya Sans", sans-serif;
    font-weight: 400;
    font-size: 36px;
    line-height: 1;
    color: var(--ink);
    letter-spacing: 1px;
    font-variant-numeric: lining-nums;
  }
</style>
</head>
<body>
  <main class="card">
    <div class="card__pattern" role="img" aria-label="Repeating decorative lattice pattern in deeper orange tones"></div>

    <svg class="card__badge" viewBox="0 0 667 700" aria-hidden="true">
      <polygon points="333,132 526,238 526,450 333,556 140,450 140,238"
               fill="var(--ink)" stroke="var(--ink)" stroke-width="28" stroke-linejoin="round"/>
      <polygon points="333,142 511,240 511,448 333,546 155,448 155,240"
               fill="none" stroke="var(--card-orange)" stroke-width="2.5" stroke-linejoin="round"/>
      <circle class="badge__mark" cx="333" cy="318" r="22" fill="var(--white)"/>
    </svg>

    <p class="text-block badge__name">Melissa Tarnow</p>

    <p class="text-block label label--address">ADDRESS</p>
    <p class="text-block contact-line address-street">4720 Halberd Lane #318</p>
    <p class="text-block contact-line address-city">San Jose</p>
    <p class="text-block contact-line address-state">California</p>
    <p class="text-block contact-line address-country">US</p>

    <p class="text-block label label--tel">TEL. NO.</p>
    <p class="text-block phone">4085172946</p>
  </main>
</body>
</html>
```